Refresh web site from year 2003

Voltaro Forma has a web site (https://vfprosjekt.no/) from early 2000 that needs to be refreshed.

Attached are company logo, favicon files, a licensed image to be used, an animation that illustrate the use of one of the products.

Target Market(s)

Industrial customers

Industry/Entity Type

Electrical Switch Board Builders, Automation Industry

Coding

Coded - Design and coding required

Number of Pages Required

3 page

Requirements
Must have
• WordPress site. Use attached animation in the front page (source file is in Adobe Animation format, if adjustments are needed). Product page for two products, "QRT" and "KV-7 Typ B".
Nice to have
• The site should focus on promoting two products QRT and KV-7 Typ B.

```html
<!DOCTYPE html>
<html lang="en">
<head>
<meta charset="utf-8">
<title>Voltaro Forma</title>
<link href="https://fonts.googleapis.com/css2?family=Poppins:wght@400;500;600;700&family=Lato:wght@400;700&family=Arimo:wght@400&display=swap" rel="stylesheet">
<style>
:root{
  --blue:#0b4a80;
  --orange:#fa9d0e;
  --ink:#2a2a2a;
  --text:#555;
  --grey:#f2f2f2;
  --white:#fff;
}
*{box-sizing:border-box;margin:0;padding:0}
html,body{width:1200px;height:3871px;overflow:hidden}
body{position:relative;font-family:'Poppins',sans-serif;color:var(--ink);background:var(--white)}
.abs{position:absolute}
.divider{position:absolute;left:50%;transform:translateX(-50%);width:100px;height:3px}
.divider::before{content:"";position:absolute;left:0;top:0;width:4px;height:3px;background:var(--orange);box-shadow:8px 0 var(--orange),16px 0 var(--orange)}
.divider::after{content:"";position:absolute;left:24px;top:0;width:76px;height:3px;background:var(--orange)}
.section-title{position:absolute;left:0;width:1200px;text-align:center;font-size:40px;font-weight:500;color:var(--ink)}
.section-title strong{color:var(--blue);font-weight:700}
.know-more{position:absolute;font-size:13px;font-weight:500;color:var(--orange);white-space:nowrap}
.know-more::before{content:"»";font-weight:700;margin-right:5px}

/* header */
.site-header{left:0;top:0;width:1200px;height:132px;background:var(--blue)}
.brand{left:55px;top:40px;width:140px;text-align:center;color:var(--white);font-size:25px;font-weight:700;line-height:30px}
.topbar{left:282px;top:16px;height:24px;display:flex;align-items:center;gap:9px;color:var(--white);font-size:14px;font-weight:500;white-space:nowrap}
.topbar .sep{width:1px;height:22px;background:#6d8fb0}
.topbar svg{margin-right:6px;vertical-align:-3px}
.socials{display:flex;gap:6px}
.socials span{display:block;width:30px;height:30px;background:var(--orange);border-radius:3px}
.header-socials{left:1022px;top:16px}
.header-rule{left:245px;top:55px;width:928px;height:2px;background:#c98a2b}
.nav-item{position:absolute;top:88px;font-size:14px;font-weight:500;color:var(--white);text-align:center;white-space:nowrap}
.nav-item.active{color:var(--orange);left:252px;width:157px;padding-bottom:10px;border-bottom:2px solid var(--orange)}
.btn-contact{left:990px;top:81px;width:190px;height:34px;background:var(--orange);color:var(--white);font-size:14px;font-weight:500;text-align:center;line-height:34px}

/* hero */
.hero{left:0;top:132px;width:1200px;height:586px;background:linear-gradient(90deg,#e4e4ec 0%,#e6e6ee 40%,#c9ccc9 60%,#a9aba4 100%)}
.hero-photo{right:0;top:0;width:700px;height:586px;background:linear-gradient(90deg,rgba(228,228,236,0) 0%,#b8bbb5 30%,#c9ccc6 55%,#9a9c92 100%)}
.hero-copy{left:35px;top:178px;width:400px;text-align:center}
.hero-copy h1{font-size:45px;line-height:44px;font-weight:700;color:var(--blue)}
.hero-copy p{margin-top:26px;font-size:21px;line-height:28px;color:var(--ink)}
.btn-explore{display:inline-block;margin-top:25px;width:118px;height:34px;line-height:34px;border-radius:17px;background:var(--orange);color:var(--white);font-size:12px;font-weight:500;border:2px solid #fff3d9}

/* about */
.about-sub{left:0;top:884px;width:1200px;font-size:16px;font-weight:600;text-align:center}
.about-text{left:305px;top:925px;width:590px;font-family:'Lato',sans-serif;font-size:12px;line-height:23.5px;color:var(--text);text-align:center}

/* products */
.products-bg{left:0;top:1172px;width:1200px;height:858px}
.product-media{width:288px;height:211px;border-radius:8px;background:var(--orange);padding:0 0 9px 0}
.product-media .frame{width:100%;height:100%;border-radius:8px 8px 6px 6px;background:var(--blue);padding:7px 10px 3px 10px}
.product-media .photo{width:100%;height:100%}
.product-title{font-size:27px;font-weight:600;line-height:37px;color:var(--ink)}
.product-sub{font-family:'Arimo',sans-serif;font-size:16px;color:var(--ink)}
.product-list{font-family:'Arimo',sans-serif;font-size:12.5px;line-height:24px;color:#444;list-style:disc}

/* services */
.service{position:absolute;top:2250px;width:270px;text-align:center}
.service h3{margin-top:22px;font-size:19px;font-weight:600;color:var(--ink)}
.service p{margin-top:15px;font-family:'Lato',sans-serif;font-size:12px;line-height:24px;color:var(--text)}

/* contact */
.contact-bg{left:0;top:2557px;width:1200px;height:819px;background:var(--grey)}
.contact-title{left:0;top:2655px;width:1200px;text-align:center;font-size:40px;line-height:54px;font-weight:500}
.contact-title strong{color:var(--blue);font-weight:700;display:block}
.info-item{position:absolute;left:170px;display:flex;align-items:center;gap:13px}
.info-icon{width:42px;height:42px;border-radius:50%;border:2px solid var(--blue);display:flex;align-items:center;justify-content:center}
.info-item h4{font-size:15px;font-weight:600;line-height:22px}
.info-item p{font-size:15px;line-height:24px}
.map{left:170px;top:3008px;width:423px;height:240px;background:linear-gradient(135deg,#dfeedd,#cfe6cc 50%,#e6efe1);border-bottom:5px solid var(--blue);border-left:3px solid var(--blue)}
.form-card{left:640px;top:2810px;width:358px;height:440px;background:var(--white);border-radius:8px;box-shadow:0 0 8px rgba(0,0,0,.25);padding:8px}
.form-inner{width:100%;height:100%;background:var(--blue);border-radius:4px;padding:26px 24px}
.form-border{width:100%;height:100%;border:3px solid var(--orange);border-radius:10px;padding:20px 17px}
.field label{display:block;font-size:11px;font-weight:500;color:var(--white);margin-bottom:4px}
.field .input{height:34px;background:var(--white);border:1px solid #999;font-family:'Lato',sans-serif;font-size:11px;color:#888;padding:10px 9px;margin-bottom:16px}
.field .input.textarea{height:74px;margin-bottom:9px}
.btn-send{height:32px;border-radius:6px;background:var(--orange);color:var(--white);font-size:11px;font-weight:500;text-align:center;line-height:32px}

/* footer */
.site-footer{left:0;top:3376px;width:1200px;height:495px;background:var(--blue);color:var(--white)}
.footer-brand{left:0;top:90px;width:1200px;text-align:center;font-size:25px;font-weight:700;line-height:30px}
.footer-nav{left:0;top:203px;width:1200px;display:flex;justify-content:center;gap:58px;font-size:14px;font-weight:500}
.footer-nav .active{color:var(--orange)}
.footer-contact{left:0;top:247px;width:1200px;display:flex;justify-content:center;align-items:center;gap:9px;font-size:14px;font-weight:500;white-space:nowrap}
.footer-contact .sep{width:1px;height:22px;background:#6d8fb0}
.footer-contact svg{margin-right:6px;vertical-align:-3px}
.footer-socials{left:554px;top:285px}
.footer-socials span{width:26px;height:26px}
.copyright{left:0;top:360px;width:1200px;text-align:center;font-size:14px;font-weight:500}
</style>
</head>
<body>

<header class="site-header abs">
  <div class="brand abs">Voltaro<br>Forma</div>
  <div class="topbar abs">
    <span><svg width="14" height="16" viewBox="0 0 14 16"><path d="M7 0a6 6 0 0 0-6 6c0 4.5 6 10 6 10s6-5.5 6-10a6 6 0 0 0-6-6zm0 8.5A2.5 2.5 0 1 1 7 3.5a2.5 2.5 0 0 1 0 5z" fill="#fa9d0e"/></svg>Brekkeveien 42 N-4820 Heimdal Norway</span>
    <span class="sep"></span>
    <span><svg width="14" height="16" viewBox="0 0 14 16"><path d="M3 1l3 3-2 2c1 2 3 4 5 5l2-2 3 3-2 3C6 15 0 9 0 3z" fill="#fa9d0e"/></svg>+47 400 18 726</span>
    <span class="sep"></span>
    <span><svg width="17" height="13" viewBox="0 0 17 13"><rect width="17" height="13" rx="2" fill="#fa9d0e"/><path d="M1 2l7.5 6L16 2" stroke="#0b4a80" stroke-width="1.5" fill="none"/></svg>post@vfprosjekt.no</span>
  </div>
  <div class="socials header-socials abs"><span></span><span></span><span></span></div>
  <div class="header-rule abs"></div>
  <nav>
    <span class="nav-item active">Home</span>
    <span class="nav-item" style="left:437px;width:120px">About Us</span>
    <span class="nav-item" style="left:617px;width:140px">Our Products</span>
    <span class="nav-item" style="left:820px;width:140px">Our Services</span>
  </nav>
  <div class="btn-contact abs">Contact Us</div>
</header>

<section class="hero abs">
  <div class="hero-photo abs" role="img" aria-label="Photograph of industrial electrical switchboard cabinets with control panels"></div>
  <div class="hero-copy abs">
    <h1>Welcome To<br>Voltaro Forma</h1>
    <p>A Production And Development<br>Company For Electronics</p>
    <span class="btn-explore">Explore More</span>
  </div>
</section>

<h2 class="section-title" style="top:797px">About <strong>Voltaro Forma</strong></h2>
<div class="divider" style="top:866px"></div>
<div class="about-sub abs">Established In 1985</div>
<p class="about-text abs">Voltaro Forma is a production and development company for electronics with an emphasis on small series production. We are today two employees with good and relevant access to additional expertise in the established network. The company was established in 1985 and has since 2001 taken over production equipment and production basis from another company in the same industry.</p>
<div class="know-more" style="left:555px;top:1060px">Know More</div>

<svg class="products-bg abs" width="1200" height="858" viewBox="0 0 1200 858"><polygon points="0,113 600,0 1200,113 1200,746 600,858 0,746" fill="#f2f2f2"/></svg>
<h2 class="section-title" style="top:1264px">Our <strong>Products</strong></h2>
<div class="divider" style="top:1333px"></div>

<div class="product-media abs" style="left:190px;top:1392px"><div class="frame"><div class="photo" role="img" aria-label="Photograph of the KV-7 Typ B relay unit, opened housing beside closed housing" style="background:linear-gradient(90deg,#e8eaee 0%,#d8dbe0 45%,#6f7d78 55%,#3f5e6e 80%,#5c6a66 100%)"></div></div></div>
<div class="product-title abs" style="left:190px;top:1618px">KV-7 Typ B</div>
<div class="product-sub abs" style="left:190px;top:1671px">UNDER VOLTAGE RELAY</div>
<div class="product-sub abs" style="left:190px;top:1714px;font-size:15px">APPLICATIONS</div>
<ul class="product-list abs" style="left:227px;top:1758px;width:320px">
  <li>The interlocking of the switch controls the power and transformer stations.</li>
  <li>Voltage indication of lines/bus bars.</li>
</ul>
<div class="know-more" style="left:213px;top:1872px">Know More</div>

<div class="product-media abs" style="left:627px;top:1392px"><div class="frame"><div class="photo" role="img" aria-label="Photograph of a row of switchboard panels with indicator lights" style="background:linear-gradient(90deg,#6b5a3c,#c9b891 30%,#a8946a 55%,#e0d3b2 75%,#5a4a30)"></div></div></div>
<div class="product-title abs" style="left:627px;top:1618px">Electrical Light Switch<br>Indicator Type QRT</div>
<div class="product-sub abs" style="left:627px;top:1709px">LED light with long lifetime!</div>
<ul class="product-list abs" style="left:665px;top:1748px;width:300px;line-height:26px">
  <li>Very long operating time due to the LED</li>
  <li>Easy mounting</li>
  <li>Reliable reading at long distance</li>
  <li>Wide angle</li>
</ul>
<div class="know-more" style="left:650px;top:1896px">Know More</div>

<h2 class="section-title" style="top:2133px">Our <strong>Services</strong></h2>
<div class="divider" style="top:2202px"></div>

<div class="service" style="left:181px">
  <svg width="40" height="42" viewBox="0 0 40 42" fill="none" stroke="#0b4a80" stroke-width="1.6"><circle cx="25" cy="13" r="9"/><path d="M21 22v5h8v-5M22 30h6"/><circle cx="10" cy="30" r="6"/><circle cx="10" cy="30" r="2"/></svg>
  <h3>Production</h3>
  <p>Small series production of electronic units in the number of 10 to 200 units.</p>
</div>
<div class="know-more" style="left:272px;top:2425px">Know More</div>

<div class="service" style="left:465px">
  <svg width="42" height="42" viewBox="0 0 42 42" fill="none" stroke="#0b4a80" stroke-width="1.6"><circle cx="21" cy="21" r="13"/><circle cx="21" cy="21" r="8"/><path d="M21 2v6M21 34v6M2 21h6M34 21h6M7.5 7.5l4 4M30.5 30.5l4 4M7.5 34.5l4-4M30.5 11.5l4-4"/></svg>
  <h3>Devolepment</h3>
  <p>Development of product concept to finished product in collaboration with a customer.</p>
</div>
<div class="know-more" style="left:555px;top:2425px">Know More</div>

<div class="service" style="left:748px">
  <svg width="40" height="42" viewBox="0 0 40 42" fill="none" stroke="#0b4a80" stroke-width="1.6"><path d="M5 5l30 32M35 5L5 37"/><rect x="3" y="3" width="8" height="8" transform="rotate(45 7 7)"/><path d="M29 31l6 6-3 1-4-4z"/></svg>
  <h3>Design</h3>
  <p>Designing of electronics and print cards for a pre-assembled and tested unit.</p>
</div>
<div class="know-more" style="left:838px;top:2425px">Know More</div>

<div class="contact-bg abs"></div>
<h2 class="contact-title abs">Get In<strong>Touch With Us</strong></h2>
<div class="divider" style="top:2780px"></div>

<div class="info-item" style="top:2818px">
  <div class="info-icon"><svg width="18" height="18" viewBox="0 0 14 16"><path d="M3 1l3 3-2 2c1 2 3 4 5 5l2-2 3 3-2 3C6 15 0 9 0 3z" fill="#0b4a80"/></svg></div>
  <div><h4>Phone</h4><p>+47 400 18 726</p></div>
</div>
<div class="info-item" style="top:2880px">
  <div class="info-icon"><svg width="18" height="14" viewBox="0 0 17 13"><rect width="17" height="13" rx="2" fill="#0b4a80"/><path d="M1 2l7.5 6L16 2" stroke="#fff" stroke-width="1.5" fill="none"/></svg></div>
  <div><h4>Email</h4><p>post@vfprosjekt.no</p></div>
</div>
<div class="info-item" style="top:2943px">
  <div class="info-icon"><svg width="16" height="19" viewBox="0 0 14 16"><path d="M7 0a6 6 0 0 0-6 6c0 4.5 6 10 6 10s6-5.5 6-10a6 6 0 0 0-6-6zm0 8.5A2.5 2.5 0 1 1 7 3.5a2.5 2.5 0 0 1 0 5z" fill="#0b4a80"/></svg></div>
  <div><h4>Address</h4><p>Brekkeveien 42 N-4820 Heimdal Norway</p></div>
</div>
<div class="map abs" role="img" aria-label="Embedded street map showing the company location"></div>

<div class="form-card abs">
  <div class="form-inner"><div class="form-border">
    <div class="field"><label>Name</label><div class="input">Name</div></div>
    <div class="field"><label>Email</label><div class="input">Email</div></div>
    <div class="field"><label>Phone</label><div class="input">Phone</div></div>
    <div class="field"><label>Message</label><div class="input textarea">Message</div></div>
    <div class="btn-send">&#9993; Send Your Message</div>
  </div></div>
</div>

<footer class="site-footer abs">
  <div class="footer-brand abs">Voltaro<br>Forma</div>
  <div class="footer-nav abs"><span class="active">Home</span><span>About Us</span><span>Our Products</span><span>Our Services</span><span>Contact Us</span></div>
  <div class="footer-contact abs">
    <span><svg width="12" height="14" viewBox="0 0 14 16"><path d="M7 0a6 6 0 0 0-6 6c0 4.5 6 10 6 10s6-5.5 6-10a6 6 0 0 0-6-6zm0 8.5A2.5 2.5 0 1 1 7 3.5a2.5 2.5 0 0 1 0 5z" fill="#fa9d0e"/></svg>Brekkeveien 42 N-4820 Heimdal Norway</span>
    <span class="sep"></span>
    <span><svg width="12" height="14" viewBox="0 0 14 16"><path d="M3 1l3 3-2 2c1 2 3 4 5 5l2-2 3 3-2 3C6 15 0 9 0 3z" fill="#fa9d0e"/></svg>+47 400 18 726</span>
    <span class="sep"></span>
    <span><svg width="15" height="11" viewBox="0 0 17 13"><rect width="17" height="13" rx="2" fill="#fa9d0e"/><path d="M1 2l7.5 6L16 2" stroke="#0b4a80" stroke-width="1.5" fill="none"/></svg>post@vfprosjekt.no</span>
  </div>
  <div class="socials footer-socials abs"><span></span><span></span><span></span></div>
  <div class="copyright abs">Copyright © 2022 VoltaroForma | Powered By VoltaroForma</div>
</footer>

</body>
</html>
```